Modern Lawfirm Business Card Design

We're looking for a business card to incorporate the newly created logo we had made.

Ideally looking for a law firm business card demonstrating, modern, minimalist, strong/bold design.

I'm open to any design honestly, but nothing "flashy".

Target Market(s)

Immigration law, family immigration, humanitarian, general legal

Industry/Entity Type

Law Firm

Contact Information for Business Card

Please use dummy information, name, street address, city, state, phone number, email, website.

Font styles to use
Serif
Sans Serif

Requirements
Must have
• Please use dummy information, name, street address, city, state, phone number, email, website.

```html
<!DOCTYPE html>
<html lang="en">
<head>
<meta charset="utf-8">
<title>Calloway Immigration Law – Business Card</title>
<link rel="stylesheet" href="https://fonts.googleapis.com/css2?family=Arimo:wght@400;700&display=swap">
<style>
  :root{
    --bg:#e6e6e4;
    --brand-blue:#1c63a3;
    --deep-blue:#17538a;
    --paper:#ffffff;
    --paper-shade:#eef0f2;
    --ink:#333a40;
    --line-dark:#1d2a3a;
  }
  *{box-sizing:border-box;margin:0;padding:0}
  html,body{width:1200px;height:1200px;overflow:hidden}
  body{background:var(--bg);font-family:"Arimo",Arial,sans-serif;position:relative}

  .card{
    position:absolute;left:250px;width:700px;height:400px;
    border-radius:34px;overflow:hidden;
    box-shadow:0 10px 28px rgba(0,0,0,.18);
  }
  .card--front{top:150px;background:var(--brand-blue)}
  .card--back{top:650px;background:var(--paper);display:flex}

  .edge-stripe{position:absolute;top:0;bottom:0;width:18px;background:var(--paper)}
  .edge-stripe::after{content:"";position:absolute;top:0;bottom:0;width:4px;background:var(--brand-blue)}
  .edge-stripe--left{left:0}
  .edge-stripe--left::after{left:6px}
  .edge-stripe--right{right:0}
  .edge-stripe--right::after{right:6px}

  .wordmark{
    position:absolute;display:flex;align-items:center;gap:14px;
    color:var(--paper);font-weight:700;letter-spacing:.08em;
  }
  .wordmark__square{width:18px;height:18px;background:var(--paper);flex:none}
  .wordmark__text{font-size:34px;line-height:1.15}
  .card--front .wordmark{left:50%;top:50%;transform:translate(-50%,-50%)}

  .back__brand{
    position:relative;width:385px;height:100%;background:var(--brand-blue);
  }
  .back__brand .edge-stripe--left{width:16px}
  .back__brand .wordmark{left:58px;top:50%;transform:translateY(-50%)}
  .back__brand .wordmark__text{font-size:28px}

  .back__details{
    position:relative;flex:1;padding:78px 34px 0 44px;
    background:linear-gradient(180deg,var(--paper) 0%,var(--paper-shade) 100%);
  }
  .top-rule{position:absolute;top:30px;left:44px;right:0;height:2px;background:var(--line-dark)}
  .person__name{color:var(--brand-blue);font-weight:700;font-size:26px;letter-spacing:.02em}
  .person__title{color:var(--ink);font-size:14px;margin-top:6px}
  .person__rule{width:170px;height:3px;background:var(--brand-blue);margin-top:14px}

  .contact{list-style:none;margin-top:40px}
  .contact li{display:flex;align-items:center;gap:10px;font-size:14px;color:var(--ink);line-height:22px}
  .contact svg{width:14px;height:14px;fill:var(--brand-blue);flex:none}
  .address{display:flex;gap:10px;margin-top:30px;font-size:14px;color:var(--ink);line-height:19px}
  .address svg{width:14px;height:14px;fill:var(--brand-blue);margin-top:2px;flex:none}
</style>
</head>
<body>

<section class="card card--front" aria-label="Card front">
  <span class="edge-stripe edge-stripe--left"></span>
  <span class="edge-stripe edge-stripe--right"></span>
  <div class="wordmark">
    <span class="wordmark__square"></span>
    <span class="wordmark__text">CALLOWAY<br>IMMIGRATION LAW</span>
  </div>
</section>

<section class="card card--back" aria-label="Card back">
  <div class="back__brand">
    <span class="edge-stripe edge-stripe--left"></span>
    <div class="wordmark">
      <span class="wordmark__square"></span>
      <span class="wordmark__text">CALLOWAY<br>IMMIGRATION LAW</span>
    </div>
  </div>
  <div class="back__details">
    <span class="top-rule"></span>
    <h1 class="person__name">JOHN DOE</h1>
    <p class="person__title">Director</p>
    <div class="person__rule"></div>
    <ul class="contact">
      <li><svg viewBox="0 0 24 24" aria-hidden="true"><path d="M6.6 10.8a15.1 15.1 0 0 0 6.6 6.6l2.2-2.2c.3-.3.7-.4 1-.2 1.1.4 2.3.6 3.6.6.6 0 1 .4 1 1V20c0 .6-.4 1-1 1A17 17 0 0 1 3 4c0-.6.4-1 1-1h3.5c.6 0 1 .4 1 1 0 1.3.2 2.5.6 3.6.1.3 0 .7-.2 1z"/></svg>1-234-567890</li>
      <li><svg viewBox="0 0 24 24" aria-hidden="true"><path d="M12 2a10 10 0 1 0 0 20 10 10 0 0 0 0-20zm6.9 6h-3a15.7 15.7 0 0 0-1.4-3.6A8 8 0 0 1 18.9 8zM12 4c.8 1.2 1.5 2.5 1.9 4h-3.8c.4-1.5 1.1-2.8 1.9-4zM4.3 14a8 8 0 0 1 0-4h3.4a16 16 0 0 0 0 4zm.8 2h3a15.7 15.7 0 0 0 1.4 3.6A8 8 0 0 1 5.1 16zm3-8h-3a8 8 0 0 1 4.4-3.6C8.9 5.6 8.4 6.8 8.1 8zM12 20c-.8-1.2-1.5-2.5-1.9-4h3.8c-.4 1.5-1.1 2.8-1.9 4zm2.3-6H9.7a14.7 14.7 0 0 1 0-4h4.6a14.7 14.7 0 0 1 0 4zm.2 5.6c.6-1.1 1.1-2.3 1.4-3.6h3a8 8 0 0 1-4.4 3.6zm1.8-5.6a16 16 0 0 0 0-4h3.4a8 8 0 0 1 0 4z"/></svg>www.callowaylaw.com</li>
      <li><svg viewBox="0 0 24 24" aria-hidden="true"><path d="M20 4H4a2 2 0 0 0-2 2v12a2 2 0 0 0 2 2h16a2 2 0 0 0 2-2V6a2 2 0 0 0-2-2zm0 4-8 5-8-5V6l8 5 8-5z"/></svg>john@callowaylaw.com</li>
    </ul>
    <div class="address">
      <svg viewBox="0 0 24 24" aria-hidden="true"><path d="M10 20v-6h4v6h5v-8h3L12 3 2 12h3v8z"/></svg>
      <p>Dummy city<br>Dummy Country Land</p>
    </div>
  </div>
</section>

</body>
</html>
```